Web Design Project

We are an IT System Integrator. We provide Norvik 500 ERP System, CRM etc. We also provide hardware, networking servicing. Please look at www.brinquot.com.sg. They provide the same service as us. We like to redesign our web site. I will attached the color that I prefer for reference.

Our website is www.ravdu.com.sg.  It has been created about 14 years ago.  We are trying to revamp it with a new look and information.   The new website must be informative, fast.    I have attached an attachment which show the color that I prefer(brownish golden).   

Our competitor (www.brinquot.com) is carrying the same trade as us.  They have all the informations In their website that we will like to have.  Therefore I recommend you to take a look at my competitor website and have a better   
understanding on the kind of information I would like to have for my new website.

This project is guarantee to the person with the best design.  We can have it guarantee.

Target Market(s)

Corporate and companies

Industry/Entity Type

Hardware

```html
<!DOCTYPE html>
<html lang="en">
<head>
<meta charset="utf-8">
<title>Ravdu Information System</title>
<link rel="stylesheet" href="https://fonts.googleapis.com/css2?family=Roboto:wght@400;500;700&family=Signika:wght@400;600&display=swap">
<style>
:root{
  --gold-light:#efe2b4;
  --gold:#c7a85e;
  --gold-dark:#8a6a26;
  --brown:#7a5a1e;
  --brown-deep:#4b3208;
  --cream:#f4eddc;
  --footer-text:#f2e6c8;
  --card:#f0efed;
  --ink:#222;
  --white:#fff;
}
*{box-sizing:border-box;margin:0;padding:0}
html,body{width:1200px;height:1011px;overflow:hidden}
body{position:relative;font-family:"Roboto",sans-serif;color:var(--ink);background:var(--cream)}
.abs{position:absolute}

/* header */
.site-header{left:0;top:0;width:1200px;height:101px;background:linear-gradient(180deg,var(--gold-light) 0%,#d9c281 50%,var(--gold-dark) 100%)}
.brand{left:285px;top:18px;display:flex;align-items:center;gap:8px;font-family:"Signika",sans-serif;font-weight:600;font-size:40px;color:var(--brown)}
.brand-dot{width:22px;height:22px;border-radius:50%;background:var(--brown)}
.util-nav{left:637px;top:23px;display:flex;gap:8px;font-size:9px;color:#3a2a08}
.search{left:785px;top:19px;width:105px;height:19px;border-radius:10px;background:var(--white);font-size:9px;color:#444;padding:4px 10px}
.search-icon{left:896px;top:20px}
.main-nav{left:480px;top:73px;display:flex;font-size:11px;font-weight:500;color:var(--white)}
.main-nav span{display:inline-block;white-space:nowrap}
.header-rule{left:0;top:101px;width:1200px;height:11px;background:linear-gradient(180deg,#9a9892,#6f6d68)}

/* hero */
.hero{left:0;top:112px;width:1200px;height:459px;background:linear-gradient(90deg,#efe5f5 0%,#d9c6e0 8%,#c7a67e 55%,#b99457 100%)}
.hero-photo{left:0;top:112px;width:660px;height:459px;background:radial-gradient(ellipse at 52% 50%,#fff3d8 0%,#8a5a4a 28%,#3b2620 60%,rgba(210,190,220,.5) 100%)}
.hero-floor{left:0;top:420px;width:1040px;height:151px;background:linear-gradient(180deg,rgba(40,120,130,.55),rgba(30,60,70,.2))}
.hero-panel{left:585px;top:112px;width:615px;height:459px;background:linear-gradient(180deg,#c4a573,#b8925a);clip-path:polygon(60px 0,100% 0,100% 100%,450px 100%,0 100px)}
.hero-title{left:600px;top:170px;width:317px;text-align:right;font-family:"Signika",sans-serif;color:var(--white);text-shadow:0 1px 2px rgba(0,0,0,.35)}
.hero-title h1{font-size:30px;font-weight:600;line-height:1.1}
.hero-title p{font-size:14px;line-height:1.45;margin-top:4px}
.thumbs{left:772px;top:300px;display:flex;gap:4px}
.thumbs span{width:34px;height:34px;border:2px solid var(--white);background:linear-gradient(135deg,#d7b2a7,#8a6b62)}
.thumbs span:nth-child(2){background:linear-gradient(135deg,#9ecbe0,#3d6f8a)}
.thumbs span:nth-child(3){background:linear-gradient(135deg,#b9c6e0,#2b2b3a)}
.thumbs span:nth-child(4){background:linear-gradient(135deg,#e0c6b0,#6a3a2a)}

.quote-bar{left:266px;top:343px;width:656px;height:34px;background:linear-gradient(180deg,#9c7a32,#7b5a1c);display:flex;align-items:center;padding-left:12px}
.quote-bar h2{font-size:17px;font-weight:700;color:var(--white);width:153px;white-space:nowrap}
.quote-bar .field{width:142px;height:18px;border-radius:9px;background:var(--white);font-size:10px;color:#888;padding:3px 10px;margin-right:12px}
.quote-go{left:888px;top:348px}

.cards{left:266px;top:385px;display:flex;gap:14px}
.card{width:154px;height:108px;background:var(--card);padding:6px 7px;position:relative;box-shadow:0 1px 3px rgba(0,0,0,.25)}
.card .mark{height:44px;display:flex;align-items:center;font-weight:700;font-size:26px;color:var(--brown)}
.card .chev{position:absolute;right:6px;top:8px}
.card h3{font-size:11px;font-weight:700;color:var(--brown);margin-top:4px}
.card p{font-size:7.5px;line-height:1.25;color:#333;margin-top:5px}

.partners{left:266px;top:506px;width:656px;height:50px;background:#efeeec;display:flex;align-items:center;padding-left:6px}
.partners b{font-size:13px;color:var(--brown);margin-right:30px}
.partners .badge-wide{width:62px;height:24px;border-radius:12px;background:#555;margin-right:32px}
.partners .badge-round{width:34px;height:34px;border-radius:50%;background:#444;margin-right:46px}

/* content */
.content{left:0;top:571px;width:1200px;height:225px;background:repeating-linear-gradient(135deg,#f6f0e2 0 3px,#efe7d3 3px 5px);border-top:1px solid #d8c89c}
.box{background:var(--white);border:1px solid #c9b684;box-shadow:0 3px 4px rgba(0,0,0,.15)}
.box-head{height:31px;background:linear-gradient(180deg,#c9ab62,#9d7c34);color:var(--white);font-size:14px;font-weight:500;padding:7px 20px}
.about{left:266px;top:586px;width:432px;height:190px}
.about .portrait{position:absolute;left:9px;top:43px;width:152px;height:131px;border:4px solid #ececec;background:linear-gradient(135deg,#555,#1a1a1a)}
.about h2{position:absolute;left:176px;top:50px;font-size:21px;font-weight:400}
.about p{position:absolute;left:176px;top:85px;width:245px;font-size:8.2px;line-height:1.3;color:#333}
.btn-more{position:absolute;left:173px;top:165px;width:59px;height:17px;background:var(--gold-dark);color:var(--white);font-size:8px;text-align:center;line-height:17px}
.news{left:712px;top:586px;width:211px;height:190px}
.dots{position:absolute;right:8px;top:12px;display:flex;gap:4px}
.dots i{width:6px;height:6px;border-radius:50%;background:#f1e9d4}
.dots i:nth-child(2){background:#3b8ab8}
.date{position:absolute;left:7px;top:43px;width:32px;height:32px;border:2px solid #a0843c;text-align:center;font-weight:700;font-size:15px;padding-top:4px}
.date-label{position:absolute;left:7px;top:79px;width:32px;text-align:center;font-size:7px;font-weight:700;line-height:1.3}
.news-photo{position:absolute;left:46px;top:43px;width:160px;height:63px;background:linear-gradient(135deg,#f3f3f3,#7a7a7a 60%,#2a2a2a)}
.news h3{position:absolute;left:9px;top:121px;font-size:11px;font-weight:500}
.news p{position:absolute;left:9px;top:140px;width:195px;font-size:7.5px;line-height:1.3;color:#333}

/* footer */
.footer-rule{left:0;top:796px;width:1200px;height:8px;background:linear-gradient(180deg,#9a9892,#6f6d68)}
.site-footer{left:0;top:804px;width:1200px;height:207px;background:linear-gradient(180deg,#4f360b,#6a4c15 60%,#52380d)}
.newsletter{left:270px;top:822px;width:146px;height:23px;border:3px solid #9a9892;background:var(--white);font-size:8px;color:#777;padding:4px 8px}
.newsletter-go{left:398px;top:827px}
.social{left:271px;top:853px;display:flex;gap:3px}
.social span{width:24px;height:24px;background:#777}
.social span:first-child{background:#3b5998}
.company{left:273px;top:887px;font-size:7.5px;line-height:1.7;font-style:normal;color:var(--footer-text)}
.company b{font-size:10px;display:block;line-height:1.4}
.footer-cols{left:440px;top:823px;display:flex;font-size:7.5px;line-height:1.68;letter-spacing:.5px;color:var(--footer-text)}
.footer-cols h4{font-size:8px;font-weight:700;margin-bottom:6px;letter-spacing:.8px}
.footer-base{left:0;top:972px;width:1200px;border-top:1px solid #8a6e38}
.copyright{left:273px;top:984px;font-size:6.5px;color:var(--footer-text)}
.legal{left:803px;top:984px;font-size:6.5px;color:var(--footer-text)}
</style>
</head>
<body>

<header class="abs site-header"></header>
<div class="abs brand"><span class="brand-dot"></span>ravdu</div>
<nav class="abs util-nav"><span>• FAQ</span><span>• Resources</span><span>• Log Incident</span></nav>
<div class="abs search">Search</div>
<svg class="abs search-icon" width="16" height="16" viewBox="0 0 16 16"><circle cx="9" cy="7" r="5" fill="none" stroke="#fff" stroke-width="1.6"/><line x1="5.5" y1="10.5" x2="1.5" y2="14.5" stroke="#fff" stroke-width="1.8"/></svg>
<nav class="abs main-nav">
  <span style="width:77px">SOLUTIONS</span><span style="width:78px">HARDWARE</span><span style="width:78px">SERVICES</span><span style="width:69px">CLIENTS</span><span style="width:75px">ABOUT US</span><span>CONTACT US</span>
</nav>
<div class="abs header-rule"></div>

<section class="abs hero"></section>
<div class="abs hero-photo" role="img" aria-label="Business team meeting in silhouette against a sunlit window"></div>
<div class="abs hero-floor"></div>
<div class="abs hero-panel"></div>
<div class="abs hero-title"><h1>Customer Relationship</h1><p>Shorten sales cycle and achieve total customer satisfaction.</p></div>
<div class="abs thumbs" role="img" aria-label="Slide thumbnails"><span></span><span></span><span></span><span></span></div>

<form class="abs quote-bar">
  <h2>GET FREE QUOTE</h2>
  <span class="field">name</span><span class="field">email</span><span class="field">mobile</span>
</form>
<svg class="abs quote-go" width="25" height="25" viewBox="0 0 26 26"><circle cx="13" cy="13" r="12" fill="#f6ecd0"/><path d="M10 7l6 6-6 6" fill="none" stroke="#7b5a1c" stroke-width="3"/></svg>

<div class="abs cards">
  <article class="card">
    <div class="mark">Norvik</div>
    <svg class="chev" width="9" height="14" viewBox="0 0 9 14"><path d="M1 1l6 6-6 6" fill="none" stroke="#7a5a1e" stroke-width="2.2"/></svg>
    <h3>NORVIK Certified</h3>
    <p>Lorem ipsum dolor sit amet, consectetur adipiscing elit. Integer id dolor magna. Aliquam elit metus, laoreet et mattis eu,</p>
  </article>
  <article class="card">
    <div class="mark"><svg width="76" height="40" viewBox="0 0 76 40"><rect x="2" y="4" width="26" height="18" rx="2" fill="none" stroke="#333" stroke-width="2"/><path d="M8 22l-2 6 7-6" fill="#333"/><circle cx="9" cy="13" r="1.6" fill="#333"/><circle cx="15" cy="13" r="1.6" fill="#333"/><circle cx="21" cy="13" r="1.6" fill="#333"/><rect x="32" y="6" width="40" height="24" rx="5" fill="none" stroke="#333" stroke-width="2.4"/><path d="M42 30l-4 8 10-8" fill="#333"/><circle cx="43" cy="18" r="2.2" fill="#7a5a1e"/><circle cx="52" cy="18" r="2.2" fill="#7a5a1e"/><circle cx="61" cy="18" r="2.2" fill="#7a5a1e"/></svg></div>
    <svg class="chev" width="9" height="14" viewBox="0 0 9 14"><path d="M1 1l6 6-6 6" fill="none" stroke="#7a5a1e" stroke-width="2.2"/></svg>
    <h3>Success Stories</h3>
    <p>Lorem ipsum dolor sit amet, consectetur adipiscing elit. Integer id dolor magna. Aliquam elit metus, laoreet et mattis eu,</p>
  </article>
  <article class="card">
    <div class="mark">Ledgra</div>
    <svg class="chev" width="9" height="14" viewBox="0 0 9 14"><path d="M1 1l6 6-6 6" fill="none" stroke="#7a5a1e" stroke-width="2.2"/></svg>
    <h3>Latest Ledgra</h3>
    <p>Lorem ipsum dolor sit amet, consectetur adipiscing elit. Integer id dolor magna. Aliquam elit metus, laoreet et mattis eu,</p>
  </article>
  <article class="card">
    <div class="mark"><svg width="60" height="44" viewBox="0 0 60 44"><g fill="#8a6540"><circle cx="20" cy="18" r="11"/><rect x="17" y="2" width="6" height="32"/><rect x="4" y="15" width="32" height="6"/><rect x="17" y="2" width="6" height="32" transform="rotate(45 20 18)"/><rect x="17" y="2" width="6" height="32" transform="rotate(-45 20 18)"/><circle cx="42" cy="32" r="7"/><rect x="40" y="22" width="4" height="20"/><rect x="32" y="30" width="20" height="4"/></g><circle cx="20" cy="18" r="4.5" fill="#f0efed"/><circle cx="42" cy="32" r="3" fill="#f0efed"/></svg></div>
    <svg class="chev" width="9" height="14" viewBox="0 0 9 14"><path d="M1 1l6 6-6 6" fill="none" stroke="#7a5a1e" stroke-width="2.2"/></svg>
    <h3>Services Beyond</h3>
    <p>Lorem ipsum dolor sit amet, consectetur adipiscing elit. Integer id dolor magna. Aliquam elit metus, laoreet et mattis eu,</p>
  </article>
</div>

<div class="abs partners">
  <b>Partners :</b>
  <span class="badge-wide"></span><span class="badge-round"></span>
  <span class="badge-wide"></span><span class="badge-round"></span>
  <span class="badge-wide"></span><span class="badge-round"></span>
</div>

<section class="abs content"></section>
<article class="abs box about">
  <div class="box-head">About Us</div>
  <div class="portrait" role="img" aria-label="Portrait of the company director"></div>
  <h2>Hello there !</h2>
  <p>Lorem ipsum dolor sit amet, consectetur adipiscing elit. Integer id dolor magna. Aliquam elit metus, laoreet et mattis eu, bibendum ac risus. Pellentesque odio nisi, iaculis eget ornare et, pulvinar eget nibh. Nunc a arcu augue. Cras hendrerit tincidunt ligula a porta. Maecenas scelerisque tortor arcu, ac porta lorem auctor id. Quisque aliquam ipsum ut enim malesuada, nec fringilla nunc dictum.</p>
  <span class="btn-more">readmore</span>
</article>
<article class="abs box news">
  <div class="box-head">Latest News</div>
  <div class="dots"><i></i><i></i><i></i><i></i><i></i></div>
  <div class="date">3</div>
  <div class="date-label">JULY<br>2013</div>
  <div class="news-photo" role="img" aria-label="Colleagues reviewing work at a laptop"></div>
  <h3>HEADER TITLE HERE</h3>
  <p>Lorem ipsum dolor sit amet, consectetur adipiscing elit. Integer id dolor magna. Aliquam elit metus, laoreet et mattis eu, bibendum ac risus. Pellentesque odio nisi, iaculis eget ornare et, pulvinar eget nibh. Nunc a arcu</p>
</article>

<div class="abs footer-rule"></div>
<footer class="abs site-footer"></footer>
<div class="abs newsletter">Enter e-mail for newsletter</div>
<svg class="abs newsletter-go" width="12" height="12" viewBox="0 0 12 12"><circle cx="6" cy="6" r="6" fill="#555"/><path d="M5 3l3 3-3 3" fill="none" stroke="#fff" stroke-width="1.5"/></svg>
<div class="abs social" role="img" aria-label="Social network links"><span></span><span></span><span></span><span></span></div>
<address class="abs company">
  <b>Ravdu Information System</b>
  Rue des Tilleuls 12 - 4100<br>Lemont - Belgium<br>Phone: +32 (0)10 55 01 23<br>Fax: +32 (0)10 55 01 24
</address>
<div class="abs footer-cols">
  <div style="width:105px"><h4>SOLUTIONS</h4>Norvik ERP Ledgra<br>Financial Management<br>Norvik ERP Ledgra<br>Financial Management<br>Norvik ERP Ledgra<br>Financial Management</div>
  <div style="width:78px"><h4>HARDWARE</h4>Submenu item 1<br>Submenu item 2<br>Submenu item 3<br>Submenu item 4<br>Submenu item 5<br>Submenu item 6</div>
  <div style="width:77px"><h4>SERVICES</h4>Submenu item 1<br>Submenu item 2<br>Submenu item 3<br>Submenu item 4<br>Submenu item 5<br>Submenu item 6</div>
  <div style="width:81px"><h4>CLIENTS</h4>Submenu item 1<br>Submenu item 2<br>Submenu item 3<br>Submenu item 4<br>Submenu item 5<br>Submenu item 6</div>
  <div style="width:85px"><h4>ABOUT US</h4>Submenu item 1<br>Submenu item 2<br>Submenu item 3<br>Submenu item 4<br>Submenu item 5<br>Submenu item 6</div>
  <div><h4>CONTACT US</h4>Inquiry<br>Location</div>
</div>
<div class="abs footer-base"></div>
<div class="abs copyright">Copyright Ravdu Solutions. All rights reserved.</div>
<div class="abs legal">Terms &amp; Conditions &nbsp;| Privacy &nbsp;| Sitemap</div>

</body>
</html>
```